Web Design for a Biotech Consulting Firm

We need a web site design for a new business based in Philadelphia called Corventa Dx. This is a consulting firm that will serve medical diagnostics industry, which is part of the life science/healthcare industry focusing on developing and marketing products that help in early detection, monitoring or management of diseases. Our consulting firm will help medical diagnostic companies to overcome key challenges in designing, evaluating and marketing new products.Our company name is Corventa Dx. Corventa is Latin word for "something" Dx represents diagnostics. The idea behind the name is that we help companies to transform the original, early product ideas ("nothing") into "something"; which is a product with full clinical utility that will help to improve health and well-being.The web site should use the visual feel of the logo (attached), be modern, simple and clean looking and represent creativity, innovation, scientific thinking and progress.
Updates

Wix Design is acceptable

Industry/Entity Type

Biotechnology

Coding

Coded - Design and coding required

Number of Pages Required

1 page

Font styles to use
Sans Serif

Requirements
Must have
• simple, clean look couple of pages
Should not have
• a lot of pages

```html
<!DOCTYPE html>
<html lang="en">
<head>
<meta charset="utf-8">
<title>Corventa Dx – Pharma and Biotech Consulting</title>
<link rel="stylesheet" href="https://fonts.googleapis.com/css2?family=Poppins:wght@400;500;600&family=Roboto+Slab:wght@500;600&display=swap">
<style>
:root{
  --blue:#1e7fe8;
  --ink:#1b1b1b;
  --text:#333;
  --muted:#f5f5f5;
  --white:#fff;
  --hero-a:#e8f1fb;
  --hero-b:#5f97d8;
  --overlay:rgba(40,40,40,.82);
}
*{box-sizing:border-box;margin:0;padding:0}
html,body{width:1200px;height:2786px;overflow:hidden}
body{font-family:"Poppins",sans-serif;color:var(--text);background:var(--white);position:relative}
a{color:inherit;text-decoration:none}

/* header */
.site-header{position:absolute;left:0;top:0;width:1200px;height:152px}
.brand-name{position:absolute;left:121px;top:50px;font-size:30px;font-weight:500;color:var(--ink);line-height:1;white-space:nowrap}
.contact-strip{position:absolute;top:28px;display:flex;align-items:center;gap:10px;font-size:17px;font-weight:600;color:var(--ink);white-space:nowrap}
.contact-strip svg{width:24px;height:24px}
.main-nav{position:absolute;top:102px;left:0;width:1200px;font-size:14px;color:var(--ink)}
.main-nav a{position:absolute;white-space:nowrap}
.main-nav .active{color:var(--blue)}

/* hero */
.hero{position:absolute;left:0;top:152px;width:1200px;height:491px;background:radial-gradient(circle at 85% 40%,#8db8ea 0%,transparent 45%),linear-gradient(120deg,var(--hero-a) 0%,#b9d2f1 45%,var(--hero-b) 100%)}
.hero-panel{position:absolute;left:121px;top:130px;width:514px;height:225px;background:var(--overlay);padding:18px 20px;color:var(--white)}
.hero-panel h1{font-weight:400;font-size:34px;line-height:40px;white-space:nowrap}
.hero-panel p{font-size:14.5px;line-height:23px;margin-top:8px;white-space:nowrap}
.hero-panel a{display:block;font-size:14px;color:var(--blue);margin-top:12px}
.hero-arrow{position:absolute;top:232px;width:30px;height:26px;background:#333;display:flex;align-items:center;justify-content:center}

/* sections */
.section-title{position:absolute;left:0;width:1200px;text-align:center;font-size:31px;font-weight:400;color:var(--ink)}
.section-title span,.about-title span{color:var(--blue)}
.section-lead{position:absolute;left:0;width:1200px;text-align:center;font-size:15px;line-height:26px;color:var(--ink)}
.feature{position:absolute;width:300px;text-align:center}
.feature-icon{width:100px;height:100px;border-radius:50%;border:4px solid var(--blue);background:radial-gradient(circle at 50% 40%,#fff 40%,#e2e2e2 100%);margin:0 auto;display:flex;align-items:center;justify-content:center;box-shadow:0 14px 10px -10px rgba(0,0,0,.18)}
.feature-icon svg{width:56px;height:56px}
.feature h3{font-family:"Roboto Slab",serif;font-weight:600;font-size:15px;color:var(--ink);margin-top:28px}
.feature p{font-size:13px;line-height:24px;margin-top:8px;color:var(--text)}
.photo-icon{width:100px;height:100px;border-radius:50%;border:4px solid var(--blue);margin:0 auto;box-shadow:0 14px 10px -10px rgba(0,0,0,.18)}

.btn{position:absolute;height:44px;display:flex;align-items:center;font-size:16px;font-weight:500;color:var(--ink);padding-left:22px;white-space:nowrap}
.btn::before{content:"";position:absolute;left:0;top:0;width:42px;height:44px;border:2px solid var(--blue);border-right:none}
.btn::after{content:"";position:absolute;left:40px;top:0;width:2px;height:8px;background:var(--blue)}

/* about */
.about{position:absolute;left:0;top:1220px;width:1200px;height:633px;background:var(--muted)}
.about-title{position:absolute;left:121px;top:112px;font-size:36px;font-weight:400;color:var(--ink);line-height:50px}
.about-copy{position:absolute;left:121px;top:180px;width:445px;font-size:13.5px;line-height:24px;color:var(--text)}
.about-copy p+p{margin-top:9px}
.about-photo{position:absolute;left:605px;top:104px;width:472px;height:449px;background:linear-gradient(160deg,#d7dde2 0%,#8e9aa3 45%,#4c5660 100%)}
.frame-line{position:absolute;background:var(--blue)}

/* footer */
.site-footer{position:absolute;left:0;top:2392px;width:1200px;height:394px;background:var(--blue);color:var(--white)}
.footer-brand{position:absolute;left:0;width:1200px;top:76px;text-align:center;font-size:26px;font-weight:500;color:var(--ink)}
.social{position:absolute;top:170px;left:0;width:1200px;display:flex;justify-content:center;gap:10px}
.social a{width:30px;height:30px;border:1px solid rgba(255,255,255,.8);display:flex;align-items:center;justify-content:center}
.social svg{width:16px;height:16px}
.footer-nav{position:absolute;top:218px;left:0;width:1200px;display:flex;justify-content:center;gap:48px;font-size:15px}
.footer-cta{position:absolute;left:394px;top:263px;width:412px;height:69px;border:1px solid rgba(255,255,255,.7);text-align:center;font-size:16px;line-height:23px;padding-top:11px}
.copyright{position:absolute;top:352px;left:0;width:1200px;text-align:center;font-size:12px}
.copyright small{font-size:10px}
</style>
</head>
<body>

<header class="site-header">
  <span class="brand-name">Corventa Dx</span>
  <div class="contact-strip" style="left:655px">
    <svg viewBox="0 0 24 24" fill="none" stroke="#1b1b1b" stroke-width="1.6"><path d="M5 3h4l2 5-3 2a12 12 0 0 0 6 6l2-3 5 2v4a2 2 0 0 1-2 2A17 17 0 0 1 3 5a2 2 0 0 1 2-2z"/></svg>
    <span>123.456.7890</span>
  </div>
  <div class="contact-strip" style="left:852px">
    <svg viewBox="0 0 24 24" fill="none" stroke="#1b1b1b" stroke-width="1.6"><rect x="3" y="6" width="18" height="13"/><path d="M3 6l9 7 9-7"/></svg>
    <span>inquiry@corventadx.com</span>
  </div>
  <nav class="main-nav">
    <a class="active" style="left:553px">Home</a>
    <a style="left:639px">About Us</a>
    <a style="left:746px">Our Services</a>
    <a style="left:878px">Resources</a>
    <a style="left:993px">Contact Us</a>
  </nav>
</header>

<section class="hero" role="img" aria-label="Blue scientific background with molecules and a DNA double helix">
  <div class="hero-panel">
    <h1>Pharma And Biotech Experts<br>For Your Success</h1>
    <p>We are redefining pharmaceutical and biotech consulting<br>by focusing scarce knowledge and proven experience<br>precisely on your goals.</p>
    <a>Click Here To Learn More</a>
  </div>
  <span class="hero-arrow" style="left:4px"><svg width="10" height="12" viewBox="0 0 10 12"><path d="M7 1L2 6l5 5" stroke="#fff" stroke-width="2" fill="none"/></svg></span>
  <span class="hero-arrow" style="left:1164px"><svg width="10" height="12" viewBox="0 0 10 12"><path d="M3 1l5 5-5 5" stroke="#fff" stroke-width="2" fill="none"/></svg></span>
</section>

<h2 class="section-title" style="top:708px">Our <span>Services</span></h2>
<p class="section-lead" style="top:762px">Our consulting firm will help medical diagnostic companies to overcome key challenges in</p>

<div class="feature" style="left:108px;top:827px">
  <div class="feature-icon"><svg viewBox="0 0 48 48" fill="none" stroke="#1b1b1b" stroke-width="2"><path d="M8 34c10-2 14-18 32-20"/><path d="M8 22c16 2 20 14 32 12"/><path d="M14 30l4 4M20 24l2 6M26 21l2 6M32 18l2 5"/></svg></div>
  <h3>Designing</h3>
  <p>Lorem ipsum dolor sit amet, sectetuer adipiscin ga mortis nisl aliquip fdafe ea commodo consequat. ...[+]</p>
</div>
<div class="feature" style="left:448px;top:827px">
  <div class="feature-icon"><svg viewBox="0 0 48 48" fill="none" stroke="#1b1b1b" stroke-width="2.4"><rect x="8" y="8" width="28" height="32" rx="2"/><path d="M14 16h16M14 22h12M14 28h8"/><path d="M40 18L26 34l-4 2 2-4 14-16z"/></svg></div>
  <h3>Evaluating</h3>
  <p>Lorem ipsum dolor sit amet, sectetuer adipiscin ga mortis nisl aliquip fdafe ea commodo consequat. ...[+]</p>
</div>
<div class="feature" style="left:788px;top:827px">
  <div class="feature-icon"><svg viewBox="0 0 48 48" fill="none" stroke="#1b1b1b" stroke-width="2"><rect x="8" y="6" width="32" height="22"/><path d="M14 12h8M14 17h14M14 22h10"/><path d="M26 42V30a3 3 0 0 1 6 0v4h4a3 3 0 0 1 3 3v5"/></svg></div>
  <h3>Marketing New Products</h3>
  <p>Lorem ipsum dolor sit amet, sectetuer adipiscin ga mortis nisl aliquip fdafe ea commodo consequat. ...[+]</p>
</div>

<a class="btn" style="left:514px;top:1099px">Contact Us Today</a>

<section class="about">
  <h2 class="about-title">About Corventa <span>Dx</span></h2>
  <div class="about-copy">
    <p>Lorem ipsum dolor sit amet, consectetuer adipiscing e, sed diam nonummy nibh euismod tincidunt ut laoreet dolore ma aliquam erat volutpat.</p>
    <p>Lorem ipsum dolor sit amet, consectetuer adipiscing e, sed diam nonummy nibh euismod tincidunt ut laoreet dolore ma aliquam erat volutpat. Ut wisi enim ad minim veniam, quis nostrud exerci tation ullamcorper suscipit lobortis nisl ut aliquip ex ea commodo consequat. Duis autem vel eum iriure dolor in hendrerivulputate velit esse molestie consequat, vel illum dolore eu feugiat nulla facilisis at vero eros et accumsan et iusto odio dissim qui blandit proesent luptatum zzril delenit augue.</p>
  </div>
  <a class="btn" style="left:121px;top:466px">Read More</a>
  <span class="frame-line" style="left:661px;top:80px;width:448px;height:5px"></span>
  <span class="frame-line" style="left:1104px;top:80px;width:5px;height:140px"></span>
  <span class="frame-line" style="left:1104px;top:386px;width:5px;height:140px"></span>
  <div class="about-photo" role="img" aria-label="Photo of a team meeting in a bright office with a presenter at a screen"></div>
</section>

<h2 class="section-title" style="top:1918px">Industry Leader – <span>Pharmaceutical &amp; Biotech Consulting</span></h2>
<p class="section-lead" style="top:1974px">We are a full service pharmaceutical and biotech consulting firm that specializes in new product planning and<br>commercial expertise to optimize product launches and brand performance.</p>

<div class="feature" style="left:114px;top:2050px">
  <div class="photo-icon" role="img" aria-label="Photo of gold puzzle pieces" style="background:radial-gradient(circle,#d9c99a 0%,#8a7a55 70%,#3c3a34 100%)"></div>
  <h3>Explore Our Capabilities</h3>
  <p>Learn how our customized services can<br>help you meet your brand goals.</p>
</div>
<div class="feature" style="left:448px;top:2050px">
  <div class="photo-icon" role="img" aria-label="Photo of a laptop showing a blog page" style="background:radial-gradient(circle,#f2f2f2 0%,#c9d3de 60%,#6f7f93 100%)"></div>
  <h3>Hear Our Perspectives</h3>
  <p>Lorem ipsum dolor sit amet, sectetuer<br>adipiscin ga mortis nisl aliquip.</p>
</div>
<div class="feature" style="left:773px;top:2050px">
  <div class="photo-icon" role="img" aria-label="Photo of colourful contact keys on a keyboard" style="background:radial-gradient(circle,#f0a070 0%,#6aa7e8 60%,#c84a6a 100%)"></div>
  <h3>Get In Touch</h3>
  <p>Contact us to learn how Corventa Dx<br>can help your organization.</p>
</div>

<a class="btn" style="left:514px;top:2293px">Contact Us Today</a>

<footer class="site-footer">
  <div class="footer-brand">Corventa Dx</div>
  <div class="social">
    <a aria-label="Share"><svg viewBox="0 0 16 16" fill="none" stroke="#fff" stroke-width="1.5"><circle cx="4" cy="8" r="2"/><circle cx="12" cy="3.5" r="2"/><circle cx="12" cy="12.5" r="2"/><path d="M5.8 7l4.4-2.5M5.8 9l4.4 2.5"/></svg></a>
    <a aria-label="Message"><svg viewBox="0 0 16 16" fill="none" stroke="#fff" stroke-width="1.5"><path d="M2 3h12v8H7l-3 3v-3H2z"/></svg></a>
    <a aria-label="Email"><svg viewBox="0 0 16 16" fill="none" stroke="#fff" stroke-width="1.5"><rect x="2" y="4" width="12" height="9"/><path d="M2 4l6 5 6-5"/></svg></a>
  </div>
  <nav class="footer-nav">
    <a>Home</a><a>About Us</a><a>Our Services</a><a>Resources</a><a>Contact Us</a>
  </nav>
  <div class="footer-cta">Contact Us To Learn<br>About How We Can Help Support Your Needs.</div>
  <p class="copyright">Copyright © 2019 Corventa Dx. All Rights Reserved. <small>Terms of Use | Privacy Policy</small></p>
</footer>

</body>
</html>
```